PlumeTrek iOS and Android mobile app design

Astronomical Dawn
The time at which the sun is 18 degrees below the horizon in the morning. Astronomical dawn is that point in time at which the sun starts lightening the sky. Prior to this time during the morning, the sky is completely dark.

My app will alert users and allow them to set reminders and alarms to when astronomical dawn starts and ends, when actual sunrise happens.

I would like something that allows the user to pick a date .. maybe show a scrollable current week to tap and see what time this even begins and ends .. then when it starts I want a countdown to sunrise graphic animation that shows until sunrise ...

Requirements
Must have
• Simplicity and elegance, Figma
Nice to have
• Material design and icons
Should not have
• Graphics that cost money

```html
<!DOCTYPE html>
<html lang="en">
<head>
<meta charset="utf-8">
<title>PlumeTrek – App Screens</title>
<link href="https://fonts.googleapis.com/css2?family=Roboto:wght@400;500;700&display=swap" rel="stylesheet">
<style>
  :root {
    --canvas: #eef0f1;
    --white: #ffffff;
    --ink: #111418;
    --ink-soft: #4a4f55;
    --field: #f4f5f6;
    --yellow: #ffc800;
    --yellow-text: #f5b800;
    --blue: #1ab0ef;
    --sky-top: #26c3fb;
    --sky-mid: #3ccaf7;
    --sea: #0aa0e0;
    --warm-light: #b9773a;
    --warm-dark: #6a4a36;
    --teal-light: #5d7c7e;
    --teal-dark: #34453d;
    --green-light: #8fa24c;
    --green-dark: #2c4a1c;
  }
  * { box-sizing: border-box; margin: 0; padding: 0; }
  html, body { width: 1200px; height: 807px; overflow: hidden; }
  body {
    background: var(--canvas);
    font-family: "Roboto", Arial, sans-serif;
    color: var(--ink);
    position: relative;
  }
  .screen {
    position: absolute;
    top: 125px;
    width: 256px;
    height: 553px;
    border-radius: 28px;
    overflow: hidden;
    background: var(--white);
    box-shadow: 0 10px 30px rgba(40, 50, 60, 0.15);
  }
  .screen--login { left: 107px; background: linear-gradient(180deg, var(--sky-top) 0%, var(--sky-mid) 55%, var(--sea) 78%, #1bb8ee 100%); }
  .screen--date { left: 470px; }
  .screen--alert { left: 833px; }

  .status-bar {
    position: absolute; top: 8px; left: 15px; right: 14px;
    display: flex; justify-content: space-between; align-items: center;
    font-size: 9px; font-weight: 500; color: var(--ink);
  }
  .screen--login .status-bar { color: var(--white); }
  .status-bar svg { width: 40px; height: 9px; fill: currentColor; }

  .app-title { position: absolute; top: 35px; font-size: 13.5px; font-weight: 500; }
  .screen--login .app-title { left: 0; right: 0; text-align: center; color: var(--white); }
  .screen--date .app-title { left: 15px; }
  .screen--alert .app-title { left: 0; right: 0; text-align: center; }

  .photo { position: absolute; }
  .photo--traveler { left: 14px; top: 64px; width: 229px; height: 256px;
    background: linear-gradient(180deg, var(--warm-light) 0%, var(--warm-dark) 100%); }
  .photo--mountain { left: 14px; top: 113px; width: 229px; height: 176px;
    background: linear-gradient(180deg, var(--teal-light) 0%, var(--teal-dark) 100%); }
  .photo--meadow { left: 0; top: 138px; width: 256px; height: 415px;
    background: linear-gradient(180deg, var(--green-light) 0%, var(--green-dark) 100%); }

  .field {
    position: absolute; left: 33px; width: 191px; height: 20px;
    background: var(--field); border-radius: 7px;
    display: flex; align-items: center; gap: 4px; padding-left: 11px;
    font-size: 6px; color: var(--ink-soft);
  }
  .field svg { width: 6px; height: 6px; fill: var(--ink-soft); }
  .field--user { top: 348px; }
  .field--pass { top: 375px; }

  .button {
    position: absolute; left: 33px; width: 192px; height: 24px;
    background: var(--yellow); border-radius: 12px;
    display: flex; align-items: center; justify-content: center;
    font-size: 9px; font-weight: 500; color: var(--ink);
  }
  .button--signin { top: 404px; }
  .button--reminder { top: 419px; box-shadow: 0 3px 6px rgba(0,0,0,0.12); }

  .login-alt { position: absolute; left: 0; right: 0; text-align: center; color: var(--white); font-size: 7px; font-weight: 500; }
  .login-alt--or { top: 437px; }
  .login-alt--register { top: 455px; }

  .home-indicator { position: absolute; left: 85px; top: 541px; width: 87px; height: 3px; border-radius: 2px; background: var(--white); }
  .screen--date .home-indicator { background: var(--blue); }

  .profile-icon { position: absolute; left: 235px; top: 38px; width: 12px; height: 12px; }

  .section-title { position: absolute; top: 78px; left: 0; right: 0; text-align: center; font-size: 11px; font-weight: 500; }
  .section-underline { position: absolute; top: 95px; left: 117px; width: 22px; height: 2px; background: var(--yellow); border-radius: 1px; }

  .date-picker {
    position: absolute; left: 33px; top: 317px; width: 191px; height: 20px;
    border-radius: 6px; background: var(--white);
    box-shadow: 0 1px 4px rgba(0,0,0,0.12);
    display: flex; align-items: center; padding: 0 9px 0 12px; gap: 3px;
    font-size: 6px; color: var(--ink-soft);
  }
  .date-picker svg.cal { width: 6px; height: 6px; fill: var(--blue); }
  .date-picker .caret { margin-left: auto; width: 5px; height: 3px; fill: var(--ink-soft); }

  .event-label { position: absolute; top: 352px; left: 0; right: 0; text-align: center; font-size: 8px; color: var(--ink-soft); }
  .event-times {
    position: absolute; top: 379px; left: 14px; right: 13px;
    display: flex; justify-content: space-between; align-items: center;
    font-size: 12px; color: var(--ink);
  }
  .time--start { color: var(--yellow-text); }
  .time--end { color: var(--blue); }
  .event-times svg { width: 23px; height: 6px; }

  .greeting {
    position: absolute; top: 70px; left: 0; right: 0; text-align: center;
    font-size: 13px; line-height: 23px; color: var(--ink-soft);
  }
</style>
</head>
<body>

  <section class="screen screen--login">
    <div class="status-bar"><span>12:00</span>
      <svg viewBox="0 0 40 9"><rect x="0" y="6" width="2" height="3"/><rect x="3" y="4" width="2" height="5"/><rect x="6" y="2" width="2" height="7"/><rect x="9" y="0" width="2" height="9"/><path d="M14 3a7 7 0 0 1 9 0l-1 1a5 5 0 0 0-7 0z M16 5a4 4 0 0 1 5 0l-2.5 3z"/><rect x="26" y="1" width="13" height="7" rx="2"/></svg>
    </div>
    <h1 class="app-title">PlumeTrek</h1>
    <div class="photo photo--traveler" role="img" aria-label="Photo of a traveller in a knit hat and jacket watching the sunset over a town"></div>
    <div class="field field--user"><svg viewBox="0 0 10 10"><circle cx="5" cy="3" r="2.5"/><path d="M0 10a5 4 0 0 1 10 0z"/></svg>User Name</div>
    <div class="field field--pass"><svg viewBox="0 0 10 10"><path d="M0 5q5-6 10 0q-5 6-10 0z"/><circle cx="5" cy="5" r="1.5" fill="#f4f5f6"/></svg>Pasword</div>
    <div class="button button--signin">Sign In</div>
    <p class="login-alt login-alt--or">or</p>
    <p class="login-alt login-alt--register">Don't Have an PlumeTrek Account Register Now</p>
    <div class="home-indicator"></div>
  </section>

  <section class="screen screen--date">
    <div class="status-bar"><span>12:00</span>
      <svg viewBox="0 0 40 9"><rect x="0" y="6" width="2" height="3"/><rect x="3" y="4" width="2" height="5"/><rect x="6" y="2" width="2" height="7"/><rect x="9" y="0" width="2" height="9"/><path d="M14 3a7 7 0 0 1 9 0l-1 1a5 5 0 0 0-7 0z M16 5a4 4 0 0 1 5 0l-2.5 3z"/><rect x="26" y="1" width="13" height="7" rx="2"/></svg>
    </div>
    <h1 class="app-title">PlumeTrek</h1>
    <svg class="profile-icon" viewBox="0 0 12 12"><circle cx="6" cy="6" r="5.3" fill="none" stroke="#1ab0ef" stroke-width="1.2"/><circle cx="6" cy="4.6" r="1.9" fill="#1ab0ef"/><path d="M2.6 9.4a4 3 0 0 1 6.8 0" fill="#1ab0ef"/></svg>
    <h2 class="section-title">Pick Date</h2>
    <div class="section-underline"></div>
    <div class="photo photo--mountain" role="img" aria-label="Photo of a hiker on a rocky summit overlooking mountains and lakes at sunrise"></div>
    <div class="date-picker">
      <svg class="cal" viewBox="0 0 10 10"><path d="M1 2h8v7H1z M1 2v2h8V2z" fill="none" stroke="#1ab0ef" stroke-width="1"/><rect x="2.5" y="0.5" width="1" height="2.5"/><rect x="6.5" y="0.5" width="1" height="2.5"/></svg>
      <span>May 25 / 2024</span>
      <svg class="caret" viewBox="0 0 6 4"><path d="M0 0h6L3 4z"/></svg>
    </div>
    <p class="event-label">Astronomical dawn</p>
    <div class="event-times">
      <span>Start at: <span class="time--start">6.46 am</span></span>
      <svg viewBox="0 0 23 6"><path d="M0 3h21M18 0.5l3 2.5l-3 2.5" fill="none" stroke="#1ab0ef" stroke-width="1"/></svg>
      <span>Ends at: <span class="time--end">7.00 am</span></span>
    </div>
    <div class="button button--reminder">Set Reminder</div>
    <div class="home-indicator"></div>
  </section>

  <section class="screen screen--alert">
    <div class="status-bar"><span>12:00</span>
      <svg viewBox="0 0 40 9"><rect x="0" y="6" width="2" height="3"/><rect x="3" y="4" width="2" height="5"/><rect x="6" y="2" width="2" height="7"/><rect x="9" y="0" width="2" height="9"/><path d="M14 3a7 7 0 0 1 9 0l-1 1a5 5 0 0 0-7 0z M16 5a4 4 0 0 1 5 0l-2.5 3z"/><rect x="26" y="1" width="13" height="7" rx="2"/></svg>
    </div>
    <h1 class="app-title">PlumeTrek</h1>
    <p class="greeting">Hi User Astronomical Down<br>Has Started</p>
    <div class="photo photo--meadow" role="img" aria-label="Photo of a lone tree on a green hill with the sun rising behind it"></div>
  </section>

</body>
</html>
```